Landing Page Design for Adult Dating Age Verification (18+)

The objective of this task is to design a visually appealing pre-landing page for the adult dating site "Pivolunda (site: https://pivolunda.example/)" with an age verification mechanism. The pre-landing page will feature two buttons that redirect visitors to the main offer. The design should also include a footer block that includes links to the terms of use, privacy policy, and contact us pages.

Design Requirements:
Develop an age verification section prominently displayed on the pre-landing page.
Design the section to include two buttons labeled "Yes" and "No" for visitors to confirm their age.
Ensure the section is visually appealing and clearly communicates the purpose of age verification.

Visual Appeal:
Create a visually appealing design that aligns with the branding and theme of the "Pivolunda" adult dating site.
Use suitable color schemes, typography, and graphics to enhance the overall visual appeal of the pre-landing page.

Layout and Navigation:
Design an engaging and intuitive layout that encourages visitors to interact with the page and proceed to the main offer.
Ensure clear and visible navigation elements that direct visitors to the main offer or provide additional information.

Responsive Design:
Develop a responsive design that provides a seamless user experience across various devices, including desktop and mobile.
Ensure the design elements and layout adapt well to different screen sizes and resolutions.

File Formats and Assets:
Deliver the final design in PSD, AI, or Sketch format, ensuring that the files are well-organized and layered.
Include any necessary images or assets used in the design, ensuring they are of high quality and optimized for web use.

```html
<!DOCTYPE html>
<html lang="en">
<head>
<meta charset="utf-8">
<title>Pivolunda – Age Verification Concepts</title>
<link href="https://fonts.googleapis.com/css2?family=Playfair+Display:wght@400;700&family=Lato:wght@400;700&display=swap" rel="stylesheet">
<style>
  :root{
    --ink-white:#ffffff;
    --plum-night:#231530;
    --plum-deep:#2c1a3d;
    --lilac-pale:#d9c3e3;
    --lilac-soft:#e8d8ef;
    --pink-accent:#f0a9e0;
    --pink-button:#efc8ec;
    --magenta-edge:#d65ed0;
    --maroon:#3a0d12;
    --crimson:#7a1622;
    --violet:#5a2a8a;
    --ocean:#1e2b7a;
    --dialog-dark:rgba(20,8,20,.55);
    --dialog-plum:rgba(40,22,58,.85);
    --dialog-light:rgba(240,228,246,.75);
  }
  *{box-sizing:border-box;margin:0;padding:0}
  html,body{width:1200px;height:2580px;overflow:hidden;background:#fff}
  body{position:relative;font-family:"Lato",Arial,sans-serif;color:var(--ink-white)}
  .screen{position:absolute;left:0;width:1200px;height:608px;overflow:hidden}
  .screen--one{top:8px}
  .screen--two{top:656px;background:var(--plum-night)}
  .screen--three{top:1288px}
  .screen--four{top:1932px;background:var(--lilac-pale)}
  .photo{position:absolute;inset:0}
  .photo--bedroom{background:radial-gradient(ellipse at 55% 35%,#8a4a44 0%,var(--crimson) 30%,var(--maroon) 70%,#1a0508 100%)}
  .photo--smoke{background:linear-gradient(100deg,#1a1a5e 0%,var(--ocean) 30%,var(--violet) 55%,#b03c9c 80%,#3a1250 100%)}
  .photo-side{position:absolute;top:0;right:0;width:700px;height:608px}
  .nav{position:absolute;top:40px;right:48px;display:flex;gap:40px;font-family:"Playfair Display",Georgia,serif;font-size:18px}
  .brand{position:absolute;display:flex;align-items:center;gap:10px;height:38px;font-family:"Playfair Display",Georgia,serif;font-size:26px;line-height:1;white-space:nowrap}
  .brand-dot{width:38px;height:38px;border-radius:50%;background:var(--pink-accent);flex:none}
  .brand--corner{top:32px;left:64px}
  .dialog{position:absolute;border:3px solid var(--pink-button);border-radius:14px;text-align:center}
  .dialog .brand{top:-46px;left:50%;transform:translateX(-50%)}
  .dialog-title{font-family:"Playfair Display",Georgia,serif;font-weight:700;font-size:30px;line-height:40px;letter-spacing:1px}
  .choices{display:flex;justify-content:center;gap:24px;margin-top:22px}
  .btn{width:100px;height:38px;border-radius:20px;border:2px solid var(--pink-button);font-family:"Playfair Display",Georgia,serif;font-size:18px;line-height:34px}
  .btn--yes{background:var(--pink-button);color:var(--plum-deep)}
  .btn--no{color:var(--ink-white)}
  .remember{display:flex;justify-content:center;align-items:center;gap:12px;margin-top:22px;font-family:"Playfair Display",Georgia,serif;font-size:17px;line-height:22px}
  .check{width:18px;height:18px;border:2px solid currentColor;border-radius:3px}
  .footer{position:absolute;font-family:"Playfair Display",Georgia,serif;font-size:14px;line-height:32px}
  .footer--center{left:0;right:0;bottom:24px;text-align:center}
  .footer--left{left:64px;bottom:40px}
  .dialog--one{left:300px;top:200px;width:600px;height:214px;padding-top:40px;background:var(--dialog-dark)}
  .dialog--two{left:64px;top:184px;width:536px;height:214px;padding-top:40px;background:var(--dialog-plum)}
  .dialog--three{left:336px;top:184px;width:552px;height:196px;padding-top:30px;background:rgba(60,40,110,.55)}
  .dialog--three .brand{top:-21px}
  .dialog--three .choices{margin-top:16px}
  .dialog--three .remember{margin-top:16px}
  .dialog--four{left:64px;top:196px;width:536px;height:214px;padding-top:40px;background:var(--dialog-light);color:var(--plum-deep);border-color:#fff}
  .dialog--four .btn{border-color:#fff}
  .dialog--four .btn--yes{background:#fff;color:var(--plum-deep)}
  .dialog--four .btn--no{color:var(--plum-deep)}
  .screen--four .brand,.screen--four .footer{color:var(--plum-deep)}
</style>
</head>
<body>

<section class="screen screen--one">
  <div class="photo photo--bedroom" role="img" aria-label="Photograph of an intimate couple on red bed sheets"></div>
  <nav class="nav"><span>Sign In</span><span>Join Now</span><span>English</span></nav>
  <div class="dialog dialog--one">
    <div class="brand"><span class="brand-dot"></span>Pivolunda</div>
    <h1 class="dialog-title">Are You Over 18 Years Of Age?</h1>
    <div class="choices"><span class="btn btn--yes">Yes</span><span class="btn btn--no">No</span></div>
    <div class="remember"><span class="check"></span>Remember Me</div>
  </div>
  <footer class="footer footer--center"><div>Privacy Policy · Terms of Use · Contact Us</div><div>Pivolunda Copyright 2023</div></footer>
</section>

<section class="screen screen--two">
  <svg class="photo-side" viewBox="0 0 700 608" role="img" aria-label="Photograph of a woman in black lingerie against pink smoke">
    <defs><linearGradient id="smokePink" x1="0" y1="0" x2="1" y2="1"><stop offset="0" stop-color="#2a1638"/><stop offset=".55" stop-color="#6a2a6e"/><stop offset="1" stop-color="#c0508e"/></linearGradient></defs>
    <path d="M40 0 C 180 120, 120 420, 20 608 L700 608 L700 0 Z" fill="url(#smokePink)"/>
    <path d="M40 0 C 180 120, 120 420, 20 608" fill="none" stroke="var(--magenta-edge)" stroke-width="10"/>
  </svg>
  <div class="brand brand--corner"><span class="brand-dot"></span>Pivolunda</div>
  <nav class="nav"><span>Sign In</span><span>Join Now</span><span>English</span></nav>
  <div class="dialog dialog--two">
    <div class="brand"><span class="brand-dot"></span>Pivolunda</div>
    <h1 class="dialog-title">Are You Over 18 Years Of Age?</h1>
    <div class="choices"><span class="btn btn--yes">Yes</span><span class="btn btn--no">No</span></div>
    <div class="remember"><span class="check"></span>Remember Me</div>
  </div>
  <footer class="footer footer--left"><div>Privacy Policy · Terms of Use · Contact Us</div><div>Pivolunda Copyright 2023</div></footer>
</section>

<section class="screen screen--three">
  <div class="photo photo--smoke" role="img" aria-label="Photograph of a woman reclining amid blue and pink smoke"></div>
  <div class="brand brand--corner"><span class="brand-dot"></span>Pivolunda</div>
  <nav class="nav"><span>Sign In</span><span>Join Now</span><span>English</span></nav>
  <div class="dialog dialog--three">
    <div class="brand"><span class="brand-dot"></span></div>
    <h1 class="dialog-title">Are You Over 18 Years Of Age?</h1>
    <div class="choices"><span class="btn btn--yes">Yes</span><span class="btn btn--no">No</span></div>
    <div class="remember"><span class="check"></span>Remember Me</div>
  </div>
  <footer class="footer footer--center"><div>Privacy Policy · Terms of Use · Contact Us</div><div>Pivolunda Copyright 2023</div></footer>
</section>

<section class="screen screen--four">
  <svg class="photo-side" viewBox="0 0 700 608" role="img" aria-label="Photograph of a woman in black lingerie against a dark red backdrop">
    <defs><linearGradient id="darkRed" x1="0" y1="0" x2="1" y2="1"><stop offset="0" stop-color="#1c1220"/><stop offset=".6" stop-color="#4a1a2a"/><stop offset="1" stop-color="#7a2030"/></linearGradient></defs>
    <path d="M40 0 C 180 120, 120 420, 20 608 L700 608 L700 0 Z" fill="url(#darkRed)"/>
    <path d="M40 0 C 180 120, 120 420, 20 608" fill="none" stroke="var(--lilac-soft)" stroke-width="10"/>
  </svg>
  <nav class="nav"><span>Sign In</span><span>Join Now</span><span>English</span></nav>
  <div class="dialog dialog--four">
    <div class="brand"><span class="brand-dot"></span>Pivolunda</div>
    <h1 class="dialog-title">Are You Over 18 Years Of Age?</h1>
    <div class="choices"><span class="btn btn--yes">Yes</span><span class="btn btn--no">No</span></div>
    <div class="remember"><span class="check"></span>Remember Me</div>
  </div>
  <footer class="footer footer--left"><div>Privacy Policy · Terms of Use · Contact Us</div><div>Pivolunda Copyright 2023</div></footer>
</section>

</body>
</html>
```